Velvet Orbit "Paper lantern"

This is my second cd project under Velvet Orbit. I want to continue to use the same Logo (the peace sign with Velvet Orbit around it) as the first incorporating it in the New design which will also feature the ufos and a person in bed dreaming. I will be needing the Cover (front and back) and back as well as the CD label. The uploaded image is the first cover and as I said I would like to incorporate the Band logo "peace sign with Velvet Orbit " in to the new design.

Target Market(s)

Music lovers

Requirements
Must have
• The Velvet Orbit logo (included in uploaded image) a person in bed sleeping (dreaming) ufos in background.
Nice to have
• Be creative!

```html
<!DOCTYPE html>
<html lang="en">
<head>
<meta charset="utf-8">
<title>Velvet Orbit — Paper Lantern — Back Cover</title>
<link rel="stylesheet" href="https://fonts.googleapis.com/css2?family=Cinzel:wght@700&family=Montserrat:wght@700&family=Arimo&display=swap">
<style>
  :root {
    --spine-black: #000000;
    --spine-text: #ffffff;
    --gold: #d9b45f;
    --gold-light: #f1d998;
    --deep-space: #0c1730;
    --night-blue: #1b2c4c;
    --sun-glow: #f7c98e;
    --ember: #b5452b;
    --floor: #3d4858;
    --track-text: #ffffff;
  }
  * { margin: 0; padding: 0; box-sizing: border-box; }
  html, body {
    width: 1200px;
    height: 939px;
    overflow: hidden;
    background: var(--spine-black);
  }
  .cover {
    position: relative;
    width: 1200px;
    height: 939px;
    background: var(--spine-black);
    overflow: hidden;
  }
  .spine {
    position: absolute;
    top: 0;
    width: 52px;
    height: 939px;
    background: var(--spine-black);
    z-index: 3;
  }
  .spine--left { left: 0; }
  .spine--right { left: 1148px; }
  .spine__label {
    position: absolute;
    left: 26px;
    white-space: nowrap;
    font-family: "Montserrat", sans-serif;
    font-weight: 700;
    font-size: 24px;
    letter-spacing: 1px;
    color: var(--spine-text);
    line-height: 1;
  }
  .spine--left .spine__label { transform: translate(-50%, -50%) rotate(-90deg); }
  .spine--right .spine__label { transform: translate(-50%, -50%) rotate(90deg); }
  .spine__label--top { top: 202px; }
  .spine__label--bottom { top: 722px; }

  .artwork {
    position: absolute;
    left: 52px;
    top: 0;
    width: 1096px;
    height: 939px;
    background:
      radial-gradient(ellipse 130px 40px at 530px 436px, rgba(255,240,200,0.95), rgba(255,220,150,0) 100%),
      linear-gradient(180deg, rgba(0,0,0,0) 428px, rgba(246,190,100,0.55) 436px, rgba(0,0,0,0) 446px),
      radial-gradient(ellipse 360px 300px at 220px 250px, rgba(247,201,142,0.85), rgba(181,69,43,0.55) 55%, rgba(181,69,43,0) 100%),
      radial-gradient(ellipse 60px 420px at 870px 520px, rgba(140,170,200,0.25), rgba(140,170,200,0) 100%),
      linear-gradient(180deg, var(--deep-space) 0%, var(--night-blue) 44%, #2a2f3c 48%, var(--floor) 75%, #4b5667 100%);
  }

  .badge {
    position: absolute;
    left: 95px;
    top: 36px;
    width: 120px;
    text-align: center;
  }
  .badge__name {
    font-family: "Cinzel", serif;
    font-weight: 700;
    font-size: 13px;
    color: rgba(200,205,215,0.7);
    letter-spacing: 1px;
  }
  .badge__ring {
    display: block;
    margin: 4px auto 0;
  }

  .band {
    position: absolute;
    left: 336px;
    top: 40px;
    width: 364px;
    text-align: center;
  }
  .band__name {
    font-family: "Cinzel", serif;
    font-weight: 700;
    font-size: 40px;
    letter-spacing: 4px;
    color: var(--gold);
    line-height: 1;
  }
  .band__ring {
    display: block;
    margin: 14px auto 0;
  }

  .title {
    position: absolute;
    left: 0;
    top: 454px;
    width: 1096px;
    text-align: center;
    font-family: "Cinzel", serif;
    font-weight: 700;
    font-size: 72px;
    letter-spacing: 22px;
    color: var(--gold-light);
    line-height: 1;
    padding-left: 22px;
  }

  .tracklist {
    position: absolute;
    top: 632px;
    list-style: none;
    font-family: "Arimo", sans-serif;
    font-size: 26px;
    line-height: 34px;
    color: var(--track-text);
  }
  .tracklist--first { left: 110px; }
  .tracklist--second { left: 640px; }
</style>
</head>
<body>
<div class="cover">
  <div class="spine spine--left">
    <span class="spine__label spine__label--top">PAPER LANTERN</span>
    <span class="spine__label spine__label--bottom">VELVET ORBIT</span>
  </div>

  <div class="artwork" role="img" aria-label="Space scene: starry night sky with a warm sunrise glow on the horizon and two blue flying saucers casting light beams">
    <div class="badge">
      <div class="badge__name">Velvet Orbit</div>
      <svg class="badge__ring" width="84" height="84" viewBox="0 0 84 84" aria-hidden="true">
        <circle cx="42" cy="42" r="37" fill="none" stroke="rgba(200,205,215,0.55)" stroke-width="7"/>
      </svg>
    </div>

    <div class="band">
      <div class="band__name">Velvet Orbit</div>
      <svg class="band__ring" width="280" height="280" viewBox="0 0 280 280" aria-hidden="true">
        <circle cx="140" cy="140" r="124" fill="none" stroke="#d9b45f" stroke-width="24"/>
      </svg>
    </div>

    <h1 class="title">PAPER LANTERN</h1>

    <ol class="tracklist tracklist--first">
      <li>1.......the name of the song</li>
      <li>2.......the name of the song</li>
      <li>3.......the name of the song</li>
      <li>4.......the name of the song</li>
      <li>5.......the name of the song</li>
      <li>6.......the name of the song</li>
      <li>7 ......the name of the song</li>
    </ol>
    <ol class="tracklist tracklist--second">
      <li>8.......the name of the song</li>
      <li>9.......the name of the song</li>
      <li>10.......the name of the song</li>
      <li>11.......the name of the song</li>
      <li>12.......the name of the song</li>
      <li>13.......the name of the song</li>
      <li>14......the name of the song</li>
    </ol>
  </div>

  <div class="spine spine--right">
    <span class="spine__label spine__label--top">VELVET ORBIT</span>
    <span class="spine__label spine__label--bottom">PAPER LANTERN</span>
  </div>
</div>
</body>
</html>
```